Web Design For Calloway Pool Service

We are working with a company that wants a website for their pool service. Some sites to use for content/competitors and inspiration:
https://sacramento.brimwaterpools.example/builder/newbuild/repair/ppc
https://coralbaypoolcareandmore.example/
https://lumoxpoolservice.example/
https://www.halvorsenspoolresurfacing.example/pool-renovation-ga/
Thank you for taking the time to consider designing a website for us. We are web developers based in Stockton, CA, USA. Most of our projects go through the same process. Understanding this process may help you win a project with us. We custom-code all of our websites in-house. We don’t have any requirements as to what tools you use for your design, but we prefer Figma files. For any design that we label as four-stars, we send it to the client for review. The client picks the final design they want us to use. Once we complete this process, we will continue to show additional clients all the four-star sites and purchase them later. Your designs will have multiple chances to sell. For better chances of success, we ask that you follow these guidelines.
IMAGES:
If you use any images or icons in the design, we ask that you have a link to the asset so we can purchase the image/icon. Most of the designs we submit do not have the customer’s images on them unless they have some great images. Be creative; show us the feeling you are trying to portray with your image choices. Use any royalty-free site you choose. We subscribe to Adobe and mainly use their images, but we can purchase images outside of Adobe. PLEASE NOTE: we will not submit designs to clients with watermarks on the images.
FONTS:
We ask that you identify the fonts used in the design. This can be done in a message if you want. We typically use Google Fonts and Adobe Fonts.
CONTENT:
We're always open to different content and ideas. We often submit designs with stock images so the client can see our vision. We typically take pictures after the website launch to use their images with our vision. Lorem Ipsum is fine for paragraphs, but we ask that you write the headers in correct English. We want to be able to show the vision and identify the sections of the website.
INSPIRATION:
We typically add a couple of links in the brief of websites we like to help you get started in your design.
REVISIONS:
We do not often ask for revisions of the designs unless we see something in the design that may not appeal to the client. If there are slight changes that we want to make, we do that in the development process.
FEEDBACK:
We rarely give feedback on designs during the design process. We are working on many website projects and do not have the time to provide feedback. We usually respond if your request is well thought out and asks specific questions, but a note asking “feedback, please” usually goes unanswered.

```html
<!DOCTYPE html>
<html lang="en">
<head>
<meta charset="utf-8">
<title>Calloway Pool Service</title>
<link href="https://fonts.googleapis.com/css2?family=Poppins:wght@400;500;600&display=swap" rel="stylesheet">
<style>
:root{
  --blue:#2fa8ee;
  --blue-deep:#2e96d8;
  --band:#2f9be0;
  --ink:#111418;
  --text:#4a4f55;
  --muted:#9aa1a8;
  --white:#ffffff;
  --footer:#050607;
  --pale:#d6ecfa;
}
*{box-sizing:border-box;margin:0;padding:0}
html,body{width:1200px;height:4886px;overflow:hidden}
body{position:relative;background:var(--white);font-family:"Poppins",sans-serif;color:var(--ink)}
.abs{position:absolute}
a{color:inherit;text-decoration:none}
.btn{position:absolute;display:flex;align-items:center;justify-content:center;border-radius:20px;font-size:14px;font-weight:500}
.btn-solid{background:var(--blue);color:var(--white)}
.btn-line{border:1.5px solid var(--blue);color:var(--blue);background:var(--white)}
.learn{color:var(--blue);font-size:15px}
.section-title{position:absolute;left:0;width:1200px;text-align:center;font-size:36px;font-weight:600;color:var(--blue);letter-spacing:.5px}
.section-intro{position:absolute;left:0;width:1200px;text-align:center;font-size:15px;line-height:25px;color:var(--text)}

/* header */
.brand{position:absolute;left:114px;top:24px;color:var(--blue);font-weight:500;line-height:1}
.brand .name{font-size:30px;letter-spacing:1px;display:block}
.brand .sub{font-size:19px;letter-spacing:4px;display:block;margin-top:4px}
.nav{position:absolute;top:41px;font-size:16px;color:var(--ink)}

/* hero */
.hero-photo{left:0;top:102px;width:1200px;height:582px;background:linear-gradient(180deg,#3d6b3a 0%,#6f8f5a 35%,#3aa6d4 60%,#1f7fb8 100%)}
.hero-card{left:557px;top:252px;width:533px;height:330px;background:rgba(255,255,255,.92);border-radius:18px}
.tagline{left:580px;top:278px;font-size:18px;font-weight:500;color:var(--blue)}
.tagline-rule{left:833px;top:291px;width:110px;height:2px;background:var(--blue)}
.hero-kicker{left:580px;top:355px;font-size:30px;font-weight:500}
.hero-title{left:580px;top:391px;font-size:42px;font-weight:600;white-space:nowrap}
.hero-title span{color:var(--blue)}
.hero-text{left:582px;top:456px;width:490px;font-size:15px;line-height:25px;color:var(--text)}

/* features */
.feature{position:absolute;top:768px;width:300px;text-align:center}
.feature svg{display:block;margin:0 auto}
.feature h3{font-size:21px;font-weight:600;margin-top:14px}
.feature p{font-size:14px;line-height:21px;color:var(--text);margin-top:10px}
.feature .learn{display:block;margin-top:12px}

/* about */
.about-photo-main{left:224px;top:1077px;width:354px;height:426px;background:linear-gradient(135deg,#3ab7d8 0%,#7fcbd6 30%,#c9a57c 60%,#b48b60 100%)}
.about-photo-inset{left:112px;top:1143px;width:282px;height:262px;border:7px solid var(--white);background:linear-gradient(160deg,#8fb6cf,#2c5a86);box-shadow:0 4px 16px rgba(0,0,0,.15)}
.years{left:110px;top:1405px;width:205px;height:98px;background:var(--blue);color:var(--white);padding:18px 0 0 18px}
.years b{font-size:28px;font-weight:600;display:block}
.years span{font-size:16px}
.kicker{font-size:36px;font-weight:600;color:var(--blue)}
.sub-heading{font-size:26px;line-height:35px;font-weight:500}
.about-kicker{left:616px;top:1124px}
.about-head{left:616px;top:1186px;width:500px}
.about-text{left:616px;top:1272px;width:475px;font-size:15px;line-height:26px;color:var(--text)}

/* why */
.why-band{left:0;top:1589px;width:600px;height:612px;background:var(--band)}
.why-photo{left:600px;top:1589px;width:600px;height:612px;background:linear-gradient(180deg,#6d7a5a 0%,#8a9688 35%,#3d7e8f 60%,#d8d8d2 85%,#c9c9c4 100%)}
.why{color:var(--white)}
.why-kicker{left:112px;top:1724px;color:var(--white)}
.why-head{left:112px;top:1789px;width:470px}
.why-text{left:112px;top:1878px;width:480px;font-size:15px;line-height:25px}
.ring{position:absolute;top:1953px;width:116px;height:116px}
.ring-label{position:absolute;top:2076px;width:220px;font-size:14px;line-height:21px;color:var(--white)}

/* services */
.svc{position:absolute;width:305px;height:298px;overflow:hidden;border-radius:4px}
.svc .photo{position:absolute;inset:0}
.svc .label{position:absolute;left:104px;bottom:0;width:201px;height:74px;background:var(--white);padding:12px 0 0 17px}
.svc .label h4{font-size:22px;font-weight:500;line-height:28px}
.svc .label .learn{font-size:15px}
.svc-more{background:linear-gradient(180deg,#0f5e95 0%,#1d86c8 55%,#0b5d92 100%);color:var(--white);text-align:center}
.svc-more p{position:absolute;left:30px;top:100px;width:245px;font-size:15px;line-height:25px}
.svc-more .btn{left:80px;top:161px;width:145px;height:36px}

/* testimonials */
.testi-band{left:0;top:3191px;width:1200px;height:370px;background:linear-gradient(180deg,#2f8ed4 0%,#3aa4e6 60%,#2b8fd6 100%)}
.testi .section-title,.testi .section-intro{color:var(--white)}
.tcard{position:absolute;top:3472px;width:305px;height:221px;background:var(--white);border-radius:8px;box-shadow:0 6px 18px rgba(0,0,0,.12);padding:22px 18px}
.tcard q{display:block;font-size:14px;line-height:24px;font-style:italic;color:var(--text);text-align:justify;quotes:"\201C" "\201D"}
.tcard .who{position:absolute;left:18px;top:140px;display:flex;align-items:center;gap:12px}
.avatar{width:60px;height:60px;border-radius:50%;background:linear-gradient(160deg,#d9b89a,#6e5446)}
.who b{display:block;font-size:22px;font-weight:500;line-height:26px}
.who small{font-size:14px;color:var(--muted)}
.quote-mark{position:absolute;right:14px;top:92px;font-size:150px;line-height:1;color:#e7e9eb;font-weight:600}
.dot{position:absolute;top:3747px;width:18px;height:18px;border-radius:50%;background:var(--pale)}
.dot.on{background:var(--blue-deep)}

/* news */
.news-img{position:absolute;width:199px;height:181px}
.news-body{position:absolute;width:245px}
.news-body h4{font-size:22px;font-weight:500;line-height:30px}
.news-body time{display:flex;align-items:center;gap:6px;font-size:12px;color:var(--muted);margin-top:8px}
.news-body p{font-size:14px;line-height:22px;color:var(--text);text-align:justify;margin-top:12px}
.news-body .learn{display:block;margin-top:6px}

/* footer */
.footer{left:0;top:4547px;width:1200px;height:313px;background:var(--footer);color:var(--white)}
.foot-brand{left:114px;top:4600px;color:var(--blue)}
.foot-text{left:112px;top:4698px;width:250px;font-size:14px;line-height:24px;text-align:justify;color:var(--white)}
.foot-col{position:absolute;top:4592px}
.foot-col h5{font-size:18px;font-weight:600;color:var(--blue);margin-bottom:13px}
.foot-col li{list-style:none;font-size:14px;line-height:29px;color:var(--white)}
.copyright{left:0;top:4860px;width:1200px;height:26px;background:var(--band);color:var(--white);font-size:14px;text-align:center;line-height:26px}
</style>
</head>
<body>

<!-- header -->
<header>
  <div class="brand"><span class="name">CALLOWAY</span><span class="sub">POOL SERVICE</span></div>
  <nav>
    <a class="nav" style="left:481px">Home</a>
    <a class="nav" style="left:564px">About</a>
    <a class="nav" style="left:647px">Services</a>
    <a class="nav" style="left:750px">Product</a>
    <a class="nav" style="left:846px">Contact</a>
  </nav>
  <a class="btn btn-solid" style="left:948px;top:32px;width:142px;height:38px">Get Started</a>
</header>

<!-- hero -->
<section class="hero">
  <div class="abs hero-photo" role="img" aria-label="Pool technician with a vacuum hose sitting beside a backyard swimming pool"></div>
  <div class="abs hero-card"></div>
  <p class="abs tagline">Refresh Relax Rejuvenate</p>
  <div class="abs tagline-rule"></div>
  <p class="abs hero-kicker">WELCOME TO</p>
  <h1 class="abs hero-title"><span>CALLOWAY</span> POOL SERVICE</h1>
  <p class="abs hero-text">Lorem ipsum dolor sit amet, consectetur adipiscing elit, sed do eiusmod tempor incididunt</p>
  <a class="btn btn-solid" style="left:582px;top:516px;width:140px;height:36px">Discover More</a>
  <a class="btn btn-line" style="left:743px;top:516px;width:142px;height:36px">Contact Us</a>
</section>

<!-- features -->
<section class="features">
  <div class="feature" style="left:123px">
    <svg width="94" height="94" viewBox="0 0 94 94" fill="none" stroke="#2fa8ee" stroke-width="3" stroke-linejoin="round" stroke-linecap="round">
      <rect x="24" y="8" width="56" height="70" rx="3"/>
      <path d="M24 18 L10 22 L18 86 L60 80"/>
      <path d="M34 24h36M34 34h36M34 44h20"/>
      <circle cx="62" cy="56" r="10"/>
      <path d="M56 64 L54 78 L62 73 L70 78 L68 64"/>
    </svg>
    <h3>Certified Company</h3>
    <p>Lorem ipsum dolor sit amet, consecte adipiscing elit, sed do eiusmod</p>
    <a class="learn">Learn More</a>
  </div>
  <div class="feature" style="left:449px">
    <svg width="94" height="94" viewBox="0 0 94 94" fill="none" stroke="#2fa8ee" stroke-width="3" stroke-linejoin="round" stroke-linecap="round">
      <path d="M10 12h22v10H10zM14 22v12h30a8 8 0 0 1 8 8v28"/>
      <path d="M32 16h10a18 18 0 0 1 18 18v36"/>
      <path d="M46 70h20v12H46z"/>
      <path d="M60 16h20v8H60zM70 24v10"/>
      <path d="M56 88 l-3 4M62 88 l3 4"/>
    </svg>
    <h3>Professional Staff</h3>
    <p>Lorem ipsum dolor sit amet, consecte adipiscing elit, sed do eiusmod</p>
    <a class="learn">Learn More</a>
  </div>
  <div class="feature" style="left:775px">
    <svg width="94" height="94" viewBox="0 0 94 94" fill="none" stroke="#2fa8ee" stroke-width="3" stroke-linecap="round">
      <circle cx="47" cy="52" r="34"/>
      <circle cx="47" cy="52" r="27"/>
      <path d="M40 8h14M47 8v10M74 22l5-5"/>
      <path d="M47 52V34M47 52l12 8"/>
    </svg>
    <h3>Fast Process</h3>
    <p>Lorem ipsum dolor sit amet, consecte adipiscing elit, sed do eiusmod</p>
    <a class="learn">Learn More</a>
  </div>
</section>

<!-- about -->
<section class="about">
  <div class="abs about-photo-main" role="img" aria-label="Aerial view of a worker cleaning a pool edge with a long pole"></div>
  <div class="abs about-photo-inset" role="img" aria-label="Smiling pool technician holding a blue hose"></div>
  <div class="abs years"><b>20+</b><span>Years Of Experience</span></div>
  <h2 class="abs kicker about-kicker">ABOUT US</h2>
  <h3 class="abs sub-heading about-head">Make Your Swimming Pool Keep Clean and Hygiene</h3>
  <p class="abs about-text">Lorem ipsum dolor sit amet, consectetur adipiscing elit, sed do eiusmod tempor incididunt ut labore et dolore magna aliqua. Quis ipsum suspendisse ultrices gravida. Risus commodo viver maecenas accumsan lacus vel facilisis. Lorem ipsum dolor sit amet, consectetur adipiscing elit, sed do eiusmod tempor inci didunt ut labore et dolore magna aliqua.</p>
  <a class="btn btn-solid" style="left:616px;top:1443px;width:142px;height:36px">More About Us</a>
</section>

<!-- why choose us -->
<section class="why">
  <div class="abs why-band"></div>
  <div class="abs why-photo" role="img" aria-label="Pool water testing kit and chemical jug beside a pool with a waterfall"></div>
  <h2 class="abs kicker why-kicker">WHY CHOOSE US</h2>
  <h3 class="abs sub-heading why-head">Make Your Swimming Pool Keep Clean and Hygiene</h3>
  <p class="abs why-text">Lorem ipsum dolor sit amet, consectetur adipiscing elit, sed do eiusmod tempor incididunt ut labore et</p>
  <svg class="ring" style="left:112px" viewBox="0 0 116 116">
    <circle cx="58" cy="58" r="52" fill="none" stroke="#1a5f93" stroke-width="8"/>
    <circle cx="58" cy="58" r="52" fill="none" stroke="#ffffff" stroke-width="8" stroke-dasharray="16.3 310" transform="rotate(-90 58 58) rotate(-18 58 58)"/>
    <text x="58" y="66" text-anchor="middle" font-family="Poppins, sans-serif" font-size="26" font-weight="600" fill="#ffffff">95%</text>
  </svg>
  <svg class="ring" style="left:347px" viewBox="0 0 116 116">
    <circle cx="58" cy="58" r="52" fill="none" stroke="#1a5f93" stroke-width="8"/>
    <circle cx="58" cy="58" r="52" fill="none" stroke="#ffffff" stroke-width="8" stroke-dasharray="16.3 310" transform="rotate(-90 58 58) rotate(-18 58 58)"/>
    <text x="58" y="66" text-anchor="middle" font-family="Poppins, sans-serif" font-size="26" font-weight="600" fill="#ffffff">95%</text>
  </svg>
  <p class="ring-label" style="left:112px">Lorem ipsum dolor sit amet, consectetur</p>
  <p class="ring-label" style="left:347px">Lorem ipsum dolor sit amet, consectetur</p>
</section>

<!-- services -->
<section class="services">
  <h2 class="section-title" style="top:2332px">OUR SERVICES</h2>
  <p class="section-intro" style="top:2390px">Lorem ipsum dolor sit amet, consectetur adipiscing elit, sed do eiusmod<br>tempor incididunt ut labore et dolore magna aliqua.</p>

  <div class="svc" style="left:110px;top:2476px">
    <div class="photo" role="img" aria-label="Pool vacuum head sweeping a sunlit pool floor" style="background:linear-gradient(150deg,#bfe6f4,#5fb4de 55%,#2d86c2)"></div>
    <div class="label"><h4>Pool Cleaning</h4><a class="learn">Learn More</a></div>
  </div>
  <div class="svc" style="left:447px;top:2476px">
    <div class="photo" role="img" aria-label="Digital water tester held above pool water" style="background:linear-gradient(160deg,#9fd7ef,#3f9fd6 60%,#1f78b8)"></div>
    <div class="label"><h4>Maintenance</h4><a class="learn">Learn More</a></div>
  </div>
  <div class="svc" style="left:783px;top:2476px">
    <div class="photo" role="img" aria-label="Hand holding a pleated pool filter cartridge" style="background:linear-gradient(150deg,#e9eef2,#bcd3e3 50%,#4c8fc4)"></div>
    <div class="label"><h4>Pool Filtration</h4><a class="learn">Learn More</a></div>
  </div>
  <div class="svc" style="left:110px;top:2808px">
    <div class="photo" role="img" aria-label="Skimmer net held over clear pool water" style="background:linear-gradient(150deg,#c4e9f7,#6cc0e6 55%,#2f90cc)"></div>
    <div class="label"><h4>Equipment</h4><a class="learn">Learn More</a></div>
  </div>
  <div class="svc" style="left:447px;top:2808px">
    <div class="photo" role="img" aria-label="Hand holding a water chemistry test kit with coloured vials" style="background:linear-gradient(150deg,#7fd0f0,#3aaee6 55%,#d9b28c)"></div>
    <div class="label"><h4>Chemical</h4><a class="learn">Learn More</a></div>
  </div>
  <div class="svc svc-more" style="left:783px;top:2808px">
    <p>Sed ut perspiciatis unde omnis iste natus error sit</p>
    <a class="btn btn-solid">More Service</a>
  </div>
</section>

<!-- testimonials -->
<section class="testi">
  <div class="abs testi-band" role="img" aria-label="Blue underwater background with ripples"></div>
  <h2 class="section-title" style="top:3328px">OUR TESTIMONIALS</h2>
  <p class="section-intro" style="top:3386px">Lorem ipsum dolor sit amet, consectetur adipiscing elit, sed do eiusmod<br>tempor incididunt ut labore et dolore magna aliqua.</p>

  <div class="tcard" style="left:112px">
    <q>Lorem ipsum dolor sit amet, consec tetur adipiscing elit, sed do eiusmod tempor incididunt ut labore et dolore magna aliqua.</q>
    <div class="quote-mark">”</div>
    <div class="who"><div class="avatar" role="img" aria-label="Customer portrait"></div><div><b>Darren</b><small>Lorem ipsum dolor</small></div></div>
  </div>
  <div class="tcard" style="left:449px">
    <q>Lorem ipsum dolor sit amet, consec tetur adipiscing elit, sed do eiusmod tempor incididunt ut labore et dolore magna aliqua.</q>
    <div class="quote-mark">”</div>
    <div class="who"><div class="avatar" role="img" aria-label="Customer portrait"></div><div><b>Darren</b><small>Lorem ipsum dolor</small></div></div>
  </div>
  <div class="tcard" style="left:785px">
    <q>Lorem ipsum dolor sit amet, consec tetur adipiscing elit, sed do eiusmod tempor incididunt ut labore et dolore magna aliqua.</q>
    <div class="quote-mark">”</div>
    <div class="who"><div class="avatar" role="img" aria-label="Customer portrait"></div><div><b>Darren</b><small>Lorem ipsum dolor</small></div></div>
  </div>

  <span class="dot" style="left:543px"></span>
  <span class="dot on" style="left:575px"></span>
  <span class="dot" style="left:605px"></span>
  <span class="dot" style="left:638px"></span>
</section>

<!-- news -->
<section class="news">
  <h2 class="section-title" style="top:3897px">NEWS &amp; ARTICLES</h2>
  <p class="section-intro" style="top:3954px">Lorem ipsum dolor sit amet, consectetur adipiscing elit, sed do eiusmod<br>tempor incididunt ut labore et dolore magna aliqua.</p>

  <div class="news-img" role="img" aria-label="Swimmer resting at the edge of a bright blue pool" style="left:110px;top:4056px;background:linear-gradient(150deg,#6fd0ef,#2aa3da 60%,#7a7f86)"></div>
  <article class="news-body" style="left:330px;top:4056px">
    <h4>Lorem ipsum dolor sit amet, consect</h4>
    <time><svg width="12" height="12" viewBox="0 0 12 12"><circle cx="6" cy="6" r="5" fill="#9aa1a8"/><path d="M6 3v3l2 1" stroke="#fff" stroke-width="1.2" fill="none"/></svg>Mar 09, 2024</time>
    <p>Lorem ipsum dolor sit amet, consectetur adipiscing elit, sed do eiusmod tempor incididunt</p>
    <a class="learn">Learn More</a>
  </article>

  <div class="news-img" role="img" aria-label="Swimmer gliding underwater in a pool" style="left:633px;top:4056px;background:linear-gradient(150deg,#1f6f86,#2a9fb8 55%,#0f4f6a)"></div>
  <article class="news-body" style="left:853px;top:4056px">
    <h4>Lorem ipsum dolor sit amet, consect</h4>
    <time><svg width="12" height="12" viewBox="0 0 12 12"><circle cx="6" cy="6" r="5" fill="#9aa1a8"/><path d="M6 3v3l2 1" stroke="#fff" stroke-width="1.2" fill="none"/></svg>Mar 09, 2024</time>
    <p>Lorem ipsum dolor sit amet, consectetur adipiscing elit, sed do eiusmod tempor incididunt</p>
    <a class="learn">Learn More</a>
  </article>

  <div class="news-img" role="img" aria-label="Children splashing and playing in a pool" style="left:110px;top:4277px;background:linear-gradient(150deg,#8fd6ee,#3fb0de 55%,#2585bd)"></div>
  <article class="news-body" style="left:330px;top:4277px">
    <h4>Lorem ipsum dolor sit amet, consect</h4>
    <time><svg width="12" height="12" viewBox="0 0 12 12"><circle cx="6" cy="6" r="5" fill="#9aa1a8"/><path d="M6 3v3l2 1" stroke="#fff" stroke-width="1.2" fill="none"/></svg>Mar 09, 2024</time>
    <p>Lorem ipsum dolor sit amet, consectetur adipiscing elit, sed do eiusmod tempor incididunt</p>
    <a class="learn">Learn More</a>
  </article>

  <div class="news-img" role="img" aria-label="Swimmer with a ring buoy in deep blue water" style="left:633px;top:4277px;background:linear-gradient(150deg,#1d7fc2,#1569a8 55%,#e06a3a)"></div>
  <article class="news-body" style="left:853px;top:4277px">
    <h4>Lorem ipsum dolor sit amet, consect</h4>
    <time><svg width="12" height="12" viewBox="0 0 12 12"><circle cx="6" cy="6" r="5" fill="#9aa1a8"/><path d="M6 3v3l2 1" stroke="#fff" stroke-width="1.2" fill="none"/></svg>Mar 09, 2024</time>
    <p>Lorem ipsum dolor sit amet, consectetur adipiscing elit, sed do eiusmod tempor incididunt</p>
    <a class="learn">Learn More</a>
  </article>
</section>

<!-- footer -->
<footer>
  <div class="abs footer"></div>
  <div class="brand foot-brand" style="top:4600px"><span class="name">CALLOWAY</span><span class="sub">POOL SERVICE</span></div>
  <p class="abs foot-text">Lorem ipsum dolor sit amet, con sectetur adipiscing elit, sed do ei usmod tempor incididunt ut labore et dolore</p>
  <div class="foot-col" style="left:470px">
    <h5>QUICK LINKS</h5>
    <ul><li>- Home</li><li>- About Us</li><li>- Services</li><li>- Products</li><li>- News &amp; Article</li><li>- Contact Us</li></ul>
  </div>
  <div class="foot-col" style="left:698px">
    <h5>SUPPORT</h5>
    <ul><li>- FAQs</li><li>- Privacy Policy</li><li>- Terms &amp; Conditions</li><li>- Cookie Policy</li><li>- History &amp; Experience</li><li>- Help Center</li></ul>
  </div>
  <div class="foot-col" style="left:984px">
    <h5>FOLLOW US</h5>
    <ul><li>- Pagebook</li><li>- Snapgram</li><li>- Chirper</li><li>- Linkpro</li><li>- Clipster</li></ul>
  </div>
  <p class="abs copyright">Copyright © 2024 Calloway Pool Service All rights reserved.</p>
</footer>

</body>
</html>
```